Property Management Company

We are looking for a sharp/modern business card design for a property management company.
We have included what should be on the business card down below in business card details.
Target Market(s)
Commercial properties, Home Owners
Industry/Entity Type
Business
Contact Information for Business Card
Name: Colin Basford | Owner
Business Name : Tern Yardworks
Slogan : A Smarter Choice
Phone : 518.555.0183
Website: www.ternyardworks.example
E-Mail : colin@ternyardworks.example
Our Services are Commercial & Residential
-Asphalt Maintenance
-Snow Management
-Landscaping
-Blacktop
Free Estimates
Free parking lot cleanup & restripe with snow removal contract

```html
<!DOCTYPE html>
<html lang="en">
<head>
<meta charset="utf-8">
<title>Tern Yardworks — Business Card</title>
<link rel="stylesheet" href="https://fonts.googleapis.com/css2?family=Open+Sans:wght@400;600;700;800&family=Oswald:wght@500&display=swap">
<style>
  :root {
    --page-bg: #d9d9d9;
    --card-white: #ffffff;
    --navy: #14244a;
    --brand-red: #c11f30;
    --service-red: #cf2a3b;
    --brand-green: #13843f;
    --text-white: #ffffff;
  }
  * { margin: 0; padding: 0; box-sizing: border-box; }
  html, body {
    width: 1200px; height: 900px; overflow: hidden;
    background: var(--page-bg);
    font-family: "Open Sans", Arial, sans-serif;
  }
  .card {
    position: absolute; left: 370px; top: 20px;
    width: 479px; height: 820px;
    background: var(--navy);
    overflow: hidden;
  }
  .card__top {
    position: absolute; left: 0; top: 0; width: 479px; height: 440px;
  }
  .slogan {
    position: absolute; top: 38px; left: 0; width: 100%;
    text-align: center;
    color: var(--brand-red);
    font-weight: 700; font-size: 17px;
    letter-spacing: 6px; text-transform: uppercase;
  }
  .brand {
    position: absolute; top: 120px; left: 0; width: 100%;
    display: flex; flex-direction: column; align-items: center; gap: 10px;
  }
  .brand__mark {
    width: 44px; height: 44px; background: var(--brand-red);
  }
  .brand__name {
    color: var(--brand-green);
    font-weight: 800; font-size: 52px; line-height: 1;
    text-transform: uppercase; text-align: center;
  }
  .brand__tagline {
    position: absolute; top: 332px; left: 0; width: 100%;
    text-align: center; color: var(--brand-green);
    font-weight: 600; font-size: 27px;
  }
  .contact {
    position: absolute; top: 474px; left: 0; width: 100%;
    text-align: center; color: var(--text-white);
  }
  .contact__name { color: var(--brand-green); font-weight: 700; font-size: 30px; line-height: 40px; }
  .contact__role { font-size: 20px; line-height: 26px; }
  .contact__phone { font-weight: 600; font-size: 34px; line-height: 46px; margin-top: 10px; }
  .contact__line { font-weight: 600; font-size: 23px; line-height: 35px; }
  .services {
    position: absolute; top: 680px; left: 20px; width: 439px;
    text-align: center; color: var(--service-red);
    font-family: "Oswald", "Arial Narrow", sans-serif;
    font-weight: 500; font-size: 17px; line-height: 26px;
    text-transform: uppercase;
  }
</style>
</head>
<body>
  <div class="card">
    <svg class="card__top" width="479" height="440" viewBox="0 0 479 440" aria-hidden="true">
      <polygon points="0,0 479,0 479,348 240,420 0,352" fill="var(--card-white)"/>
      <polygon points="0,352 240,420 479,348 479,356 240,428 0,360" fill="var(--brand-green)"/>
      <polygon points="0,360 240,428 479,356 479,366 240,440 0,372" fill="var(--brand-red)"/>
    </svg>

    <p class="slogan">A Smarter Choice</p>

    <div class="brand">
      <span class="brand__mark"></span>
      <span class="brand__name">Tern<br>Yardworks</span>
    </div>
    <p class="brand__tagline">Asphalt &amp; Snow Removal</p>

    <div class="contact">
      <p class="contact__name">Colin Basford</p>
      <p class="contact__role">Owner</p>
      <p class="contact__phone">518.555.0183</p>
      <p class="contact__line">www.ternyardworks.example</p>
      <p class="contact__line">colin@ternyardworks.example</p>
    </div>

    <p class="services">
      Commercial &amp; Residential -Asphalt Maintenance<br>
      -Snow Management -Landscaping<br>
      -Blacktop Free Estimates -Free Parking Lot Cleanup &amp;<br>
      Restripe with Snow Removal Contract
    </p>
  </div>
</body>
</html>
```